Food Safety 1-California workers only

3.25" by 4.5" Black and White Magazine Ad
This ad is to train California workers only.
Workers will be trained on: Food Safety, FSMA (Food Safety Modernization Act), using equipment safety, food processing production skills, worker safety, supervisory skills, communication skills.
"FREE TRAINING", The company does the training or Keystone Learning will provide the training.
Training grants range from $100,000 to $400,000.
Companies must be in business for profit.
Companies must train 200 employees or more.
This program is for California workers only.
Incumbent or new-hires are eligible.

Target Market(s)

California food processors, farms, food packaging, food processors, companies under FSMA, food safety, food production who need to train employees.

Industry/Entity Type

Food Production

Font styles to use
Serif
Sans Serif

Colors

Designer to choose colors to be used in the design.

Requirements
Must have
• This is a 3.25 inch by 4.5 inch magazine ad. It must be black and white. No color.
• The deliverable must be in basic PhotoShop. The ad does not need to include any graphics and be text only if needed. If you have a black and white graphic that will show well.
• Look at www.KLGFoodSafety..com
• Use the text from "MEALBOX-Photoshop-052018" file as your starting point.
Nice to have
• A black and white graphic about food. See www.KLGFoodSafety.com
Should not have
• No color.

```html
<!DOCTYPE html>
<html lang="en">
<head>
<meta charset="utf-8">
<title>Free Training – Keystone Learning</title>
<link rel="stylesheet" href="https://fonts.googleapis.com/css2?family=Anton&family=Barlow:wght@400;500;700&display=swap">
<style>
  :root {
    --ink: #000000;
    --paper: #ffffff;
    --divider: #6b6b6b;
  }
  * { margin: 0; padding: 0; box-sizing: border-box; }
  html, body { width: 867px; height: 1200px; overflow: hidden; background: var(--paper); }
  .ad {
    position: relative;
    width: 867px; height: 1200px;
    background: var(--ink);
    font-family: "Barlow", "Helvetica Neue", Arial, sans-serif;
    color: var(--ink);
  }
  .offer-panel {
    position: absolute; left: 3px; top: 3px;
    width: 532px; height: 1194px;
    background: var(--paper);
  }
  .panel-divider {
    position: absolute; left: 535px; top: 0;
    width: 14px; height: 1200px;
    background: var(--divider);
  }
  .headline {
    position: absolute; left: 63px; top: 30px;
    font-family: "Anton", Impact, sans-serif;
    font-size: 120px; line-height: 1.09;
    text-transform: uppercase;
    letter-spacing: 0.5px;
  }
  .rule {
    position: absolute; left: 66px;
    width: 400px; height: 11px;
    background: var(--ink);
  }
  .rule--top { top: 325px; }
  .rule--bottom { top: 592px; }
  .topics {
    position: absolute; left: 0; top: 378px;
    width: 532px; list-style: none;
    text-align: center;
    font-size: 33px; line-height: 42.6px;
    letter-spacing: 0.5px;
  }
  .qualify-title {
    position: absolute; left: 0; top: 686px;
    width: 532px; text-align: center;
    font-size: 26px; font-weight: 500;
  }
  .qualify-list {
    position: absolute; left: 48px; top: 746px;
    width: 470px; list-style: none;
    font-size: 27.5px; line-height: 40px; font-weight: 500;
  }
  .qualify-list li { padding-left: 18px; text-indent: -18px; }
  .qualify-list li::before { content: "- "; }
  .tagline {
    position: absolute; left: 549px; top: 360px;
    width: 318px; text-align: center;
    font-family: "Anton", Impact, sans-serif;
    font-size: 40px; line-height: 55px;
    color: var(--paper);
    text-transform: uppercase;
  }
  .contact {
    position: absolute; left: 566px; top: 678px;
    width: 290px; color: var(--paper);
  }
  .contact-title {
    width: 278px; text-align: center;
    margin-left: -12px;
    font-size: 26px; font-weight: 500;
    margin-bottom: 20px;
  }
  .contact-details {
    font-style: normal;
    font-size: 27.5px; line-height: 40px; font-weight: 500;
  }
  .contact-links {
    list-style: none; margin-top: 4px;
    font-size: 20px; line-height: 28.7px; font-weight: 700;
  }
</style>
</head>
<body>
<main class="ad">
  <section class="offer-panel">
    <h1 class="headline">Free<br>Training</h1>
    <div class="rule rule--top"></div>
    <ul class="topics">
      <li>FOOD SAFETY</li>
      <li>FSMA</li>
      <li>PRODUCTION SKILLS</li>
      <li>WORKER SAFETY</li>
    </ul>
    <div class="rule rule--bottom"></div>
    <h2 class="qualify-title">How to qualify:</h2>
    <ul class="qualify-list">
      <li>Train California Workers Only</li>
      <li>Trainees must earn $11/hour</li>
      <li>Full-time workers only</li>
      <li>Employees must attend at least 8 Hours of training</li>
      <li>You must train 200 or more employees</li>
      <li>Incumbent or New-Hire workers eligible</li>
      <li>Seasonal workers are eligible</li>
    </ul>
  </section>
  <div class="panel-divider"></div>
  <p class="tagline">You do the<br>training and<br>the state<br>pays for it!</p>
  <section class="contact">
    <h2 class="contact-title">Contact:</h2>
    <address class="contact-details">
      Daniel Hart<br>
      Keystone Learning<br>
      Company, Inc.<br>
      2150<br>
      Harbor Crest Drive<br>
      Suite 310<br>
      Irvine, CA 92614
    </address>
    <ul class="contact-links">
      <li>www.KLGCAL.com</li>
      <li>www.KLGFoodSafety.com</li>
      <li>Dan.Hart@KLGCAL.com</li>
      <li>Phone: (949) 555-0147</li>
    </ul>
  </section>
</main>
</body>
</html>
```